Professional website for psychological services

Create a professional, easy to navigate website using soothing coastal images and incorporate company logo in design. Website is for a small private clinic that provides psychological services and must be appealing to professional men and women. A website I really like is www.velmorlodge.example I would love something like similar.

Target Market(s)

Professional men and women seeking psychological services

Industry/Entity Type

Mental Health

Number of Pages Required

5+ page

Requirements
Must have
• The website must incorporate the logo provided. The name of the company/website is Brindle Oak Wellness Aftercare. Colors must compliment the logo, must be coastal and soothing yet very professional. I would like a website like www.velmorlodge.example
• Pages will be:Home, Services, FAQ and Contact Us. The images included of the building and office are for the contact us page. Under the tab Servies: Individual Psychotherapy, Family Therapy, EMDR I will provide specific content for each.
Nice to have
• I want the website to be easy to navigate and the font easy to read. The writing on the logo is very light and I'm open to changing it slightly if it will be better aesthetically.
Should not have
• Please no pictures of any swimsuits, alcoholic beverages, etc. This is a professional psychological clinic.

```html
<!DOCTYPE html>
<html lang="en">
<head>
<meta charset="utf-8">
<title>Brindle Oak Wellness Aftercare</title>
<link rel="stylesheet" href="https://fonts.googleapis.com/css2?family=Roboto+Condensed:wght@300;400;700&family=Roboto:wght@400;500&family=Dancing+Script:wght@500&display=swap">
<style>
:root{
  --aqua:#1aa8c8;
  --aqua-light:#3cc3df;
  --sea-deep:#0f4f5c;
  --sea-mid:#1e7a86;
  --sand:#f8f5f0;
  --ink:#444444;
  --title:#555555;
  --body:#666666;
  --tan:#a08a6e;
  --white:#ffffff;
}
*{margin:0;padding:0;box-sizing:border-box}
html,body{width:1200px;height:2490px;overflow:hidden;background:var(--white)}
body{position:relative;font-family:"Roboto",Arial,sans-serif;color:var(--ink)}
.abs{position:absolute}
.top-rule{left:0;top:0;width:1200px;height:2px;background:var(--aqua)}
.brand{left:0;width:1200px;text-align:center;font-family:"Roboto Condensed",Arial,sans-serif;font-weight:400;font-size:34px;color:var(--aqua);line-height:1}
.brand-header{top:56px}
.brand-footer{top:2156px}
.social{display:flex;gap:11px}
.social span{display:block;width:42px;height:42px;border:1.5px solid #666;border-radius:50%}
.social-header{left:836px;top:54px}
.social-footer{left:499px;top:2318px}
.nav-rule{left:160px;top:139px}
.nav{font-family:"Roboto Condensed",Arial,sans-serif;font-size:14px;color:#333;text-transform:uppercase}
.nav a{position:absolute;color:#333;text-decoration:none;transform:translateX(-50%);white-space:nowrap}
.nav a.active{color:var(--aqua)}
.nav-header{top:157px;left:0}
.nav-footer{top:2265px;left:0}
.hero{left:0;top:186px;width:1200px;height:407px;background:linear-gradient(180deg,#4d5a55 0%,#2a6d75 22%,var(--sea-mid) 45%,var(--sea-deep) 100%)}
.hero-frame{left:229px;top:219px;width:272px;height:344px;background:#f2f2f2}
.hero-photo{left:244px;top:232px;width:242px;height:316px;background:linear-gradient(160deg,#cfe0ea 0%,#e8e2d6 55%,#e6cc52 100%)}
.hero-play{left:338px;top:360px}
.hero-kicker{left:572px;top:348px;font-family:"Roboto Condensed",Arial,sans-serif;font-weight:300;font-size:37px;color:var(--white)}
.hero-title{left:562px;top:386px;font-family:"Roboto Condensed",Arial,sans-serif;font-weight:700;font-size:68px;color:var(--white);letter-spacing:-0.5px}
.about{left:0;top:593px;width:1200px;height:426px;background:var(--sand)}
.eyebrow{font-family:"Roboto Condensed",Arial,sans-serif;font-weight:300;font-size:31px;color:var(--title);line-height:1}
.about-eyebrow{left:160px;top:648px}
.about-title{left:160px;top:675px;font-family:"Roboto Condensed",Arial,sans-serif;font-weight:700;font-size:46px;color:var(--ink);line-height:1}
.about-rule{left:385px;top:692px}
.copy{font-size:11.3px;line-height:16px;color:var(--body);text-align:justify}
.about-p1{left:160px;top:728px;width:574px}
.about-p2{left:160px;top:802px;width:574px}
.btn{display:flex;align-items:center;justify-content:center;border:2px solid var(--tan);border-radius:20px;font-family:"Roboto Condensed",Arial,sans-serif;font-size:12px;color:var(--ink);text-transform:uppercase;width:92px;height:38px}
.about-btn{left:160px;top:923px}
.portrait{left:770px;top:647px;width:271px;height:316px;background:linear-gradient(180deg,#5f8c3f 0%,#3f6b2c 40%,#2c2a2e 100%);box-shadow:0 4px 12px rgba(0,0,0,.25)}
.feature-img{left:160px;width:371px;height:260px}
.img-speaking{top:1076px;background:linear-gradient(135deg,#8a5a3e 0%,#d8d6d2 50%,#3b3a3c 100%)}
.img-press{top:1373px;background:linear-gradient(135deg,#2c3552 0%,#8a8fae 45%,#1c1c24 100%)}
.feature-title{left:561px;font-family:"Roboto Condensed",Arial,sans-serif;font-weight:700;font-size:30px;color:var(--title);line-height:1}
.ft1{top:1095px}
.ft2{top:1392px}
.feature-copy{left:561px;width:478px}
.fc1a{top:1140px}.fc1b{top:1212px}.fc2a{top:1437px}.fc2b{top:1509px}
.fb1{left:561px;top:1278px}
.fb2{left:561px;top:1576px}
.divider{left:160px;top:1355px;width:879px;height:1px;background:#e6e6e6}
.contact{left:0;top:1690px;width:1200px;height:395px;background:linear-gradient(110deg,var(--aqua-light) 0%,#2fb6d4 45%,var(--aqua) 100%)}
.contact-eyebrow{left:0;top:1740px;width:1200px;text-align:center;font-family:"Roboto Condensed",Arial,sans-serif;font-weight:700;font-size:30px;color:var(--white);line-height:1}
.contact-title{left:0;top:1768px;width:1200px;text-align:center;font-family:"Roboto Condensed",Arial,sans-serif;font-weight:700;font-size:50px;color:var(--white);line-height:1}
.field{border-bottom:2px solid var(--white);font-family:"Roboto",Arial,sans-serif;font-weight:500;font-size:11.5px;color:var(--white);text-transform:uppercase;padding-bottom:10px}
.f-name{left:160px;top:1854px;width:270px}
.f-email{left:463px;top:1854px;width:271px}
.f-phone{left:767px;top:1854px;width:272px}
.f-message{left:160px;top:1927px;width:879px}
.submit{left:549px;top:1994px;width:100px;height:38px;border:2px solid var(--white);display:flex;align-items:center;justify-content:center;font-family:"Roboto Condensed",Arial,sans-serif;font-weight:700;font-size:20px;color:var(--white)}
.bottom-bar{left:0;top:2414px;width:1200px;height:76px;background:var(--aqua);display:flex;align-items:center;justify-content:center;font-family:"Roboto",Arial,sans-serif;font-weight:500;font-size:11px;color:var(--white);text-transform:uppercase}
</style>
</head>
<body>
<div class="abs top-rule"></div>

<header>
  <div class="abs brand brand-header">Brindle Oak</div>
  <div class="abs social social-header" aria-label="Social links"><span></span><span></span><span></span><span></span></div>
  <svg class="abs nav-rule" width="880" height="12" viewBox="0 0 880 12">
    <line x1="5" y1="6" x2="875" y2="6" stroke="#1aa8c8" stroke-width="2"/>
    <rect x="1" y="2" width="8" height="8" fill="#1aa8c8" transform="rotate(45 5 6)"/>
    <rect x="871" y="2" width="8" height="8" fill="#1aa8c8" transform="rotate(45 875 6)"/>
  </svg>
  <nav class="abs nav nav-header">
    <a class="active" style="left:412px">Home</a>
    <a style="left:532px">Services</a>
    <a style="left:644px">FAQ</a>
    <a style="left:767px">Contact Us</a>
  </nav>
</header>

<section>
  <div class="abs hero" role="img" aria-label="Aerial view of ocean waves breaking on a rocky shore"></div>
  <div class="abs hero-frame"></div>
  <div class="abs hero-photo" role="img" aria-label="Video still of a woman enjoying the sea breeze"></div>
  <svg class="abs hero-play" width="56" height="56" viewBox="0 0 56 56">
    <circle cx="28" cy="28" r="27" fill="rgba(255,255,255,.35)"/>
    <polygon points="22,17 40,28 22,39" fill="rgba(255,255,255,.85)"/>
  </svg>
  <div class="abs hero-kicker">RECOVERY</div>
  <div class="abs hero-title">AFTER CARE</div>
</section>

<section>
  <div class="abs about"></div>
  <div class="abs eyebrow about-eyebrow">ABOUT</div>
  <h1 class="abs about-title">BRINDLE OAK</h1>
  <svg class="abs about-rule" width="350" height="6" viewBox="0 0 350 6">
    <line x1="0" y1="3" x2="350" y2="3" stroke="#e4e0d8" stroke-width="1"/>
    <rect x="320" y="1" width="30" height="4" fill="#222"/>
  </svg>
  <p class="abs copy about-p1">Integer consectetur augue sit amet lacinia vehicula. Ut tincidunt massa et ipsum rutrum dictum ac in purus. Morbi sit amet leo eget nibh dignissim posuere. Morbi ut purus ultricies, pharetra ipsum consequat, luctus nisi. Donec sodales eros tellus, ac consequat magna tempor at.</p>
  <p class="abs copy about-p2">Praesent mattis scelerisque dolor, et condimentum quam. Morbi tincidunt eleifend viverra. Integer consectetur augue sit amet lacinia vehicula. Ut tincidunt massa et ipsum rutrum dictum ac in purus. Morbi sit amet leo eget nibh dignissim posuere. Integer consectetur augue sit amet lacinia vehicula. Ut tincidunt massa et ipsum rutrum dictum ac in purus. Morbi sit amet leo eget nibh dignissim posuere. Morbi ut purus ultricies, pharetra ipsum consequat, luctus nisi. Donec sodales eros tellus, ac consequat magna tempor at. Praesent mattis scelerisque dolor, et condimentum quam. Morbi tincidunt eleifend viverra.</p>
  <div class="abs btn about-btn">Read More</div>
  <div class="abs portrait" role="img" aria-label="Portrait of the clinic's lead psychologist outdoors"></div>
</section>

<section>
  <div class="abs feature-img img-speaking" role="img" aria-label="Speaker presenting to a seated audience"></div>
  <h2 class="abs feature-title ft1">SPEAKING AND TRAINING</h2>
  <p class="abs copy feature-copy fc1a">Integer consectetur augue sit amet lacinia vehicula. Ut tincidunt massa et ipsum rutrum dictum ac in purus. Morbi sit amet leo eget nibh dignissim posuere. Morbi ut purus ultricies, pharetra ipsum consequat, luctus nisi. Donec sodales eros tellus, ac consequat magna tempor at.</p>
  <p class="abs copy feature-copy fc1b">Integer consectetur augue sit amet lacinia vehicula. Ut tincidunt massa et ipsum rutrum dictum ac in purus. Morbi sit amet leo eget nibh dignissim posuere. Morbi ut purus ultricies, pharetra ipsum consequat, luctus nisi.</p>
  <div class="abs btn fb1">Read More</div>

  <div class="abs divider"></div>

  <div class="abs feature-img img-press" role="img" aria-label="Press microphones gathered at a podium"></div>
  <h2 class="abs feature-title ft2">IN THE PRESS</h2>
  <p class="abs copy feature-copy fc2a">Integer consectetur augue sit amet lacinia vehicula. Ut tincidunt massa et ipsum rutrum dictum ac in purus. Morbi sit amet leo eget nibh dignissim posuere. Morbi ut purus ultricies, pharetra ipsum consequat, luctus nisi. Donec sodales eros tellus, ac consequat magna tempor at.</p>
  <p class="abs copy feature-copy fc2b">Integer consectetur augue sit amet lacinia vehicula. Ut tincidunt massa et ipsum rutrum dictum ac in purus. Morbi sit amet leo eget nibh dignissim posuere. Morbi ut purus ultricies, pharetra ipsum consequat, luctus nisi.</p>
  <div class="abs btn fb2">Read More</div>
</section>

<section>
  <div class="abs contact" role="img" aria-label="Soft aerial view of turquoise shallow water"></div>
  <div class="abs contact-eyebrow">CONTACT</div>
  <h2 class="abs contact-title">BRINDLE OAK</h2>
  <div class="abs field f-name">Name</div>
  <div class="abs field f-email">Email</div>
  <div class="abs field f-phone">Phone</div>
  <div class="abs field f-message">Message</div>
  <div class="abs submit">SUBMIT</div>
</section>

<footer>
  <div class="abs brand brand-footer">Brindle Oak</div>
  <nav class="abs nav nav-footer">
    <a class="active" style="left:435px">Home</a>
    <a style="left:541px">Services</a>
    <a style="left:637px">FAQ</a>
    <a style="left:745px">Contact Us</a>
  </nav>
  <div class="abs social social-footer" aria-label="Social links"><span></span><span></span><span></span><span></span></div>
  <div class="abs bottom-bar">2019 Brindle Oak. All Rights Reserved</div>
</footer>
</body>
</html>
```